***Dappled Fern Lash Studio is in need of a web site makeover***

I need a makeover for my existing web site. www.dappled-fern.com

Please help!!!! Thanks 😁

Dappled Fern Lash Studio is an eyelash extension salon. In addition, we also provide skincare services (facials, waxing, etc). Our web site needs to appear professional and intuitive. In addition, allowing for ease of online booking is of utmost importance.

The client web site experience:
- esthetically pleasing and makes sense
- clearly recognize brand (Dappled Fern)
- easy to follow web pages
- easy to book appointments online
- easy to sign up for email updates
- easily locate services menu and pricing

Target Market(s)

Dappled Fern Lash Studio offers eyelash extension services, as well as various skincare services (I.e. facials, waxing, etc.)

Industry/Entity Type

Beauty Salon

Number of Pages Required

5+ page

Font styles to use
Sans Serif
Script

Colors
000000
fee3d5
eaeaea
ffffff

Requirements
Must have
• - Home page with static contact information
• - Services page (menu of services and pricing)
• - Photo gallery page
• - Contact page
• - Q&A page
Nice to have
• Professional, classy, intuitive and simple for clients to be able to book online.

```html
<!DOCTYPE html>
<html lang="en">
<head>
<meta charset="utf-8">
<title>Dappled Fern Lash Studio</title>
<link rel="stylesheet" href="https://fonts.googleapis.com/css2?family=Open+Sans:ital,wght@0,300;0,400;0,600;0,700;1,400&family=Cormorant+Garamond:ital,wght@1,500&display=swap">
<style>
  :root{
    --black:#000000;
    --ink:#222222;
    --muted:#6d6d6d;
    --peach:#fee3d5;
    --peach-deep:#e9a98a;
    --grey:#eaeaea;
    --white:#ffffff;
    --footer:#1c1c1c;
  }
  *{box-sizing:border-box;margin:0;padding:0}
  html,body{width:1200px;height:2460px;overflow:hidden;background:var(--white)}
  body{position:relative;font-family:"Open Sans",Arial,sans-serif;color:var(--ink)}
  .abs{position:absolute}
  p{font-size:13px;line-height:1.75;color:var(--muted)}

  /* top info bar */
  .topbar{left:0;top:0;width:1200px;height:26px;border-bottom:1px solid var(--grey);font-size:11px;color:var(--muted)}
  .topbar span{position:absolute;top:6px;display:flex;align-items:center;gap:6px}
  .topbar svg{width:11px;height:11px;fill:var(--ink)}

  /* brand row */
  .brand{left:104px;top:48px;display:flex;align-items:center;gap:10px;font-size:30px;font-weight:700;color:var(--black)}
  .brand i{width:14px;height:14px;border-radius:50%;background:var(--peach-deep);display:block}
  .hours{right:104px;top:58px;font-size:11px;color:var(--muted)}
  .hours b{color:var(--peach-deep);font-weight:600}

  /* nav */
  .nav{left:0;top:118px;width:1200px;height:34px;background:var(--black);display:flex;justify-content:center;gap:0}
  .nav a{color:var(--white);text-decoration:none;font-size:13px;line-height:34px;padding:0 34px}
  .nav a.active{background:#2b2b2b}

  /* hero */
  .hero{left:0;top:152px;width:1200px;height:440px;background:linear-gradient(110deg,#cfc6c2 0%,#b8aba6 35%,#d9c4b8 60%,#8f7d76 100%)}
  .hero-title{left:640px;top:50px;font-size:40px;font-weight:300;color:var(--white);line-height:1.25}
  .arrow{top:200px;width:34px;height:34px;border-radius:50%;background:rgba(0,0,0,.65)}
  .arrow svg{width:34px;height:34px;stroke:var(--white);fill:none;stroke-width:2}
  .booking{left:196px;top:18px;width:232px;height:400px;background:var(--white);padding:16px 18px;box-shadow:0 2px 10px rgba(0,0,0,.25)}
  .booking h3{font-size:14px;font-weight:600;text-align:center;margin-bottom:12px}
  .booking label{display:block;font-size:11px;color:var(--ink);margin-top:10px}
  .booking .field{height:24px;border:1px solid #d6d6d6;margin-top:4px;font-size:10px;color:#aaa;padding:4px 6px}
  .booking .area{height:52px}
  .btn{display:inline-block;background:var(--black);color:var(--white);font-size:12px;font-weight:600;padding:8px 18px}
  .booking .btn{position:absolute;left:76px;bottom:18px;font-size:14px;padding:10px 22px}

  /* section headings */
  .heading{left:0;width:1200px;text-align:center;font-family:"Cormorant Garamond",Georgia,serif;font-style:italic;font-weight:500;font-size:40px;color:var(--ink)}
  .heading span{position:relative;padding:0 24px}
  .heading span::before,.heading span::after{content:"";position:absolute;top:50%;width:110px;height:1px;background:#9a9a9a}
  .heading span::before{right:100%}
  .heading span::after{left:100%}

  .rule{left:104px;width:992px;height:1px;background:#d8d8d8}

  /* about */
  .about-photo{left:108px;top:728px;width:324px;height:252px;background:linear-gradient(135deg,#3a3f44,#7e8a93 55%,#2e3236)}
  .about-text{left:462px;top:724px;width:636px}
  .about-btn{left:462px;top:948px}

  /* services */
  .service{top:1180px;width:300px;text-align:center}
  .service .photo{width:156px;height:156px;border-radius:50%;margin:0 auto;background:radial-gradient(circle at 45% 40%,#f3d4c3,#d79f86 70%,#a9735d)}
  .service h4{font-size:20px;font-weight:400;margin:18px 0 8px}
  .service p{font-size:11.5px;line-height:1.65}
  .service .price{font-size:12px;color:var(--peach-deep);font-weight:600;margin:10px 0}

  /* herbal band */
  .herbal{left:0;top:1584px;width:1200px;height:200px;background:linear-gradient(90deg,#efe7e2 0%,#e6d8cf 45%,#c99b78 75%,#b27a55 100%)}
  .herbal h2{position:absolute;left:178px;top:62px;font-size:46px;font-weight:300;color:var(--ink);letter-spacing:1px}
  .herbal h2 b{font-weight:300;color:var(--peach-deep)}
  .herbal small{position:absolute;left:470px;top:126px;font-size:12px;color:var(--ink)}

  /* gallery */
  .gallery-intro{left:160px;top:1936px;width:880px;text-align:center;font-size:12px}
  .tile{top:1996px;width:228px;height:244px;background:linear-gradient(160deg,#f1dfd4,#d5a68b)}

  /* newsletter */
  .newsletter{left:0;top:2310px;width:1200px;height:64px;background:var(--grey)}
  .newsletter h5{position:absolute;left:100px;top:22px;font-size:17px;font-weight:400;color:#555;letter-spacing:.5px}
  .newsletter h5 b{font-weight:400;color:var(--peach-deep)}
  .newsletter .input{position:absolute;left:648px;top:18px;width:300px;height:28px;background:var(--white);border:1px solid #cfcfcf}
  .newsletter .btn{position:absolute;left:972px;top:18px;padding:6px 16px}

  /* footer */
  .footer{left:0;top:2398px;width:1200px;height:62px;background:var(--footer);color:#bdbdbd;font-size:11px}
  .footer .copy{position:absolute;left:100px;top:24px}
  .footer .social{position:absolute;right:100px;top:20px;display:flex;gap:10px}
  .footer .social i{display:block;width:20px;height:20px;border-radius:50%;border:1px solid #8a8a8a}
</style>
</head>
<body>

<div class="abs topbar">
  <span style="left:104px"><svg viewBox="0 0 24 24"><path d="M12 2a7 7 0 0 0-7 7c0 5 7 13 7 13s7-8 7-13a7 7 0 0 0-7-7zm0 9.5A2.5 2.5 0 1 1 12 6.5a2.5 2.5 0 0 1 0 5z"/></svg>214 Larkspur Ave, Fairhaven 40210</span>
  <span style="left:820px"><svg viewBox="0 0 24 24"><path d="M6.6 10.8a15 15 0 0 0 6.6 6.6l2.2-2.2a1 1 0 0 1 1-.25 11.4 11.4 0 0 0 3.6.57 1 1 0 0 1 1 1V20a1 1 0 0 1-1 1A17 17 0 0 1 3 4a1 1 0 0 1 1-1h3.5a1 1 0 0 1 1 1c0 1.25.2 2.45.57 3.6a1 1 0 0 1-.25 1z"/></svg>(555) 014-2287</span>
  <span style="left:960px"><svg viewBox="0 0 24 24"><path d="M3 5h18v14H3zm2 2v.5l7 4.5 7-4.5V7z"/></svg>hello@dappled-fern.com</span>
</div>

<div class="abs brand"><i></i>Dappled Fern</div>
<div class="abs hours">We're open Mon - Sat &nbsp;|&nbsp; Hours: <b>9am - 7pm</b></div>

<nav class="abs nav">
  <a class="active">Home</a><a>About</a><a>Services</a><a>Our team</a><a>Gallery</a><a>pricing</a><a>Contact</a>
</nav>

<section class="abs hero" role="img" aria-label="Close-up photo of a client relaxing during an eyelash treatment">
  <h1 class="abs hero-title">We are eyelashes<br>improvement salon</h1>
  <div class="abs arrow" style="left:52px"><svg viewBox="0 0 34 34"><path d="M19 11l-6 6 6 6"/></svg></div>
  <div class="abs arrow" style="right:52px"><svg viewBox="0 0 34 34"><path d="M15 11l6 6-6 6"/></svg></div>
  <form class="abs booking">
    <h3>Book An Appointment</h3>
    <label>Choose A Day</label><div class="field">Select a date</div>
    <label>Choose Time</label><div class="field">Select a time</div>
    <label>Contact Method</label><div class="field">Phone or email</div>
    <label>Observations</label><div class="field area">Notes</div>
    <span class="btn">Book Now</span>
  </form>
</section>

<h2 class="abs heading" style="top:636px"><span>About Our Dappled Fern</span></h2>
<div class="abs about-photo" role="img" aria-label="Photo of lash extension tools and products on a table"></div>
<p class="abs about-text">Dappled Fern Lash Studio is a calm, welcoming space devoted to beautiful, natural looking eyelash extensions and gentle skincare. Our certified lash artists take time to understand the look you want, then map each set to the shape of your eyes so it feels light and lasts. Alongside lashes we offer facials, waxing and skin treatments using clean, herbal products chosen for sensitive skin. Every visit begins with a short consultation and ends with aftercare advice, so you leave confident and cared for. Booking online takes only a minute, and our team is always happy to answer questions about services, pricing or fills. We believe looking after yourself should feel simple, relaxing and personal, from the moment you arrive until your next appointment.</p>
<span class="abs btn about-btn">Read more</span>

<div class="abs rule" style="top:1046px"></div>

<h2 class="abs heading" style="top:1096px"><span>Services</span></h2>

<div class="abs service" style="left:110px">
  <div class="photo" role="img" aria-label="Photo of a client receiving a facial mask"></div>
  <h4>Facials</h4>
  <p>Deep cleansing facials that refresh, hydrate and calm the skin, tailored to your skin type with soothing herbal masks and a relaxing massage.</p>
  <div class="price">From $65</div>
  <span class="btn">Read more</span>
</div>
<div class="abs service" style="left:450px">
  <div class="photo" role="img" aria-label="Photo of a waxing treatment in progress"></div>
  <h4>Waxing</h4>
  <p>Quick, gentle waxing for brows, face and body using warm low temperature wax that is kind to skin and leaves it smooth for weeks.</p>
  <div class="price">From $20</div>
  <span class="btn">Read more</span>
</div>
<div class="abs service" style="left:790px">
  <div class="photo" role="img" aria-label="Photo of a skincare treatment with a therapist"></div>
  <h4>Skincare</h4>
  <p>Targeted skincare treatments for clarity, tone and glow, with expert advice and take home routines to keep results lasting longer.</p>
  <div class="price">From $45</div>
  <span class="btn">Read more</span>
</div>

<section class="abs herbal" role="img" aria-label="Photo of a woman with long curly hair and natural makeup">
  <h2>WE USE ONLY <b>HERBAL</b> PRODUCTS</h2>
  <small>Gentle on skin, kind to lashes.</small>
</section>

<h2 class="abs heading" style="top:1856px"><span>Gallery</span></h2>
<p class="abs gallery-intro">Take a look at recent lash sets, facials and skincare results from our studio. Every look is created by our team to suit the client, from soft natural lashes to full glamorous volume.</p>
<div class="abs tile" style="left:104px" role="img" aria-label="Gallery photo of a woman with natural lash extensions"></div>
<div class="abs tile" style="left:358px;background:linear-gradient(160deg,#f0e2d8,#c98a6e)" role="img" aria-label="Gallery photo of a fruit facial mask treatment"></div>
<div class="abs tile" style="left:612px;background:linear-gradient(160deg,#e8e2de,#9c8a82)" role="img" aria-label="Gallery photo of lash extensions being applied"></div>
<div class="abs tile" style="left:866px;background:linear-gradient(160deg,#e9c7a8,#b5683f)" role="img" aria-label="Gallery photo of a woman with curly red hair and full lashes"></div>

<section class="abs newsletter">
  <h5>SUBSCRIBE TO OUR <b>NEWSLETTER</b> FOR SPECIAL OFFERS</h5>
  <div class="input"></div>
  <span class="btn">Sign up</span>
</section>

<footer class="abs footer">
  <span class="copy">Copyright &copy; 2015 Dappled Fern. All rights reserved.</span>
  <div class="social"><i></i><i></i><i></i><i></i></div>
</footer>

</body>
</html>
```